Website for "Centro de Tecnicas Verdales"

We need a new web design for an enterprise dedicated to environment and energy saving engineering, based in Monterrey, Mexico.
They offer consulting services, mainly to enhance building designs, and they are also resellers for several products in the energy saving field.

The final design should be oriented to engineers and architects, and should communicate professionalism, innovation, environment care.

Here is the website of a partner enterprise, which does pretty much the same:

http://www.brisatermica.example/

Target Market(s)

mainly architects and engineers looking for solutions on energy efficiency building

Industry/Entity Type

Environment

Requirements
Must have
• Entry page must be quite graphical and intuitive, must have a "products listing" and a "projects portfolio".

```html
<!DOCTYPE html>
<html lang="en">
<head>
<meta charset="utf-8">
<title>Centro de Tecnicas Verdales — Energy &amp; Building Solutions</title>
<link href="https://fonts.googleapis.com/css2?family=Roboto:wght@300;400;500;700&display=swap" rel="stylesheet">
<style>
  :root {
    --navy: #2d3e50;
    --link: #2a6fb0;
    --green: #a6cc38;
    --orange: #f47320;
    --purple: #4a3f7a;
    --cyan: #00a9d4;
    --ink: #1a1a1a;
    --white: #ffffff;
    --page: #ffffff;
  }
  * { box-sizing: border-box; margin: 0; padding: 0; }
  html, body { width: 1000px; height: 1200px; overflow: hidden; background: var(--page); }
  body { position: relative; font-family: 'Roboto', Arial, sans-serif; color: var(--ink); }
  a { color: var(--link); text-decoration: none; }
  .abs { position: absolute; }

  /* header */
  .utility-links { right: 283px; top: 17px; font-size: 12px; color: var(--ink); white-space: nowrap; }
  .search { left: 726px; top: 12px; width: 155px; height: 25px; border: 2px solid var(--navy); border-radius: 4px; background: var(--white); overflow: hidden; }
  .search-field { position: absolute; left: 8px; top: 4px; font-size: 9px; color: #9a9a9a; }
  .search-button { position: absolute; right: 0; top: 0; width: 24px; height: 21px; background: var(--navy); }
  .brand { left: 120px; top: 62px; display: flex; align-items: center; gap: 16px; }
  .brand-dot { width: 56px; height: 56px; border-radius: 50%; background: var(--green); }
  .brand-name { font-size: 34px; font-weight: 700; color: var(--navy); letter-spacing: 0.2px; }

  /* navigation */
  .main-nav { left: 119px; top: 175px; width: 762px; height: 43px; background: var(--navy); border-radius: 7px; display: flex; justify-content: center; }
  .main-nav a { color: var(--white); font-size: 16px; line-height: 43px; padding: 0 15px; border-right: 1px solid #3f5266; }
  .main-nav a:last-child { border-right: none; }

  /* hero */
  .hero { left: 119px; top: 227px; width: 762px; height: 345px; border-radius: 7px; overflow: hidden;
    background: linear-gradient(180deg, #b9b8c0 0%, #a8a8ae 40%, #8b8d90 62%, #6f7275 80%, #55585a 100%); }
  .hero-pager { position: absolute; left: 8px; bottom: 5px; display: flex; gap: 8px; }
  .hero-pager span { width: 18px; height: 18px; background: rgba(255,255,255,0.22); color: var(--white); font-size: 11px; text-align: center; line-height: 18px; }

  /* panels */
  .tab { position: absolute; height: 36px; color: var(--white); font-size: 16px; font-weight: 700; display: flex; align-items: center; padding-left: 20px;
    clip-path: polygon(4% 0, 91% 0, 100% 100%, 0 100%); border-radius: 6px 0 0 0; }
  .panel { position: absolute; border-radius: 0 8px 8px 8px; }
  .panel-inner { position: absolute; left: 8px; top: 8px; right: 8px; bottom: 8px; background: var(--white); border-radius: 8px; overflow: hidden; }
  .tab-icon { width: 20px; height: 20px; margin-right: 9px; }

  .news-tab { left: 119px; top: 580px; width: 173px; background: var(--navy); }
  .tech-tab { left: 293px; top: 580px; width: 171px; background: var(--navy); }
  .news-panel { left: 119px; top: 615px; width: 505px; height: 214px; background: var(--navy); border-radius: 0 8px 8px 8px; }
  .news-photo { left: 9px; top: 8px; width: 178px; height: 179px; border: 1px solid #222; background: linear-gradient(180deg, #8d86b4 0%, #a69bc1 50%, #c79fb6 85%, #b28aa6 100%); }
  .news-title { left: 204px; top: 6px; font-size: 16px; font-weight: 700; color: var(--link); text-decoration: underline; }
  .news-body { left: 204px; top: 36px; width: 285px; font-size: 10.8px; line-height: 12.4px; letter-spacing: -0.1px; }
  .news-more { left: 204px; top: 172px; font-size: 11px; color: var(--link); }

  .monitor-tab { left: 633px; top: 580px; width: 171px; background: var(--green); }
  .monitor-panel { left: 633px; top: 615px; width: 248px; height: 214px; background: var(--green); }

  .products-tab { left: 119px; top: 837px; width: 172px; background: var(--orange); padding-left: 26px; }
  .products-panel { left: 119px; top: 872px; width: 249px; height: 213px; background: var(--orange); }
  .product-photo { left: 63px; top: 20px; width: 107px; height: 113px; border-radius: 4px; background: linear-gradient(135deg, #3a3d42 0%, #16181b 60%, #2a2c30 100%); }
  .product-points { left: 10px; top: 150px; font-size: 11px; line-height: 12.5px; }
  .product-more { right: 10px; top: 177px; font-size: 11px; color: var(--link); }

  .portfolio-tab { left: 376px; top: 837px; width: 172px; background: var(--purple); }
  .portfolio-panel { left: 376px; top: 872px; width: 248px; height: 213px; background: var(--purple); }
  .portfolio-photo { left: 0; top: 0; width: 100%; height: 100%; background: radial-gradient(ellipse at 50% 35%, #9b94c6 0%, #4b4a78 45%, #2b2a45 100%); }
  .portfolio-cta { left: 0; width: 100%; top: 142px; text-align: center; color: var(--white); font-size: 20px; font-weight: 300; line-height: 24px; }

  .efficiency-tab { left: 633px; top: 837px; width: 171px; background: var(--cyan); }
  .efficiency-panel { left: 633px; top: 872px; width: 248px; height: 213px; background: var(--cyan); }

  .chart { position: absolute; left: 0; top: 0; }

  /* footer */
  .footer-links { left: 119px; top: 1121px; font-size: 12.5px; font-weight: 700; color: var(--link); }
  .footer-links a { color: var(--link); }
  .legal { left: 119px; top: 1146px; width: 760px; font-size: 8px; line-height: 10px; color: #222; }
  .legal-note { left: 119px; top: 1174px; font-size: 8px; color: #222; }
</style>
</head>
<body>

<header>
  <div class="abs utility-links"><a href="#">Contact Us</a> | <a href="#">Careers</a></div>
  <div class="abs search">
    <span class="search-field">enter keywords here</span>
    <span class="search-button">
      <svg width="24" height="21" viewBox="0 0 24 21"><circle cx="11" cy="9" r="5.5" fill="none" stroke="#fff" stroke-width="1.6"/><line x1="15" y1="13" x2="19" y2="17" stroke="#fff" stroke-width="1.8"/></svg>
    </span>
  </div>
  <div class="abs brand">
    <span class="brand-dot"></span>
    <span class="brand-name">Centro de Tecnicas Verdales</span>
  </div>
  <nav class="abs main-nav">
    <a href="#">ABOUT</a><a href="#">PRODUCTS</a><a href="#">BENEFITS</a><a href="#">CUSTOMERS</a><a href="#">SOLUTIONS</a>
  </nav>
</header>

<section class="abs hero" role="img" aria-label="Photo of a parking lot shaded by a steel canopy carrying rows of solar panels">
  <div class="hero-pager"><span>1</span><span>2</span><span>3</span><span>4</span><span>5</span></div>
</section>

<div class="tab news-tab">
  <svg class="tab-icon" viewBox="0 0 20 20"><circle cx="10" cy="10" r="10" fill="#fff"/><polyline points="5.5,8 10,12.5 14.5,8" fill="none" stroke="#2d3e50" stroke-width="2.4"/></svg>NEWS
</div>
<div class="tab tech-tab">
  <svg class="tab-icon" viewBox="0 0 20 20"><circle cx="10" cy="10" r="10" fill="#fff"/><polyline points="8,5.5 12.5,10 8,14.5" fill="none" stroke="#2d3e50" stroke-width="2.4"/></svg>TECHNOLOGY
</div>
<section class="panel news-panel">
  <div class="panel-inner">
    <div class="abs news-photo" role="img" aria-label="Photo of a high-voltage transmission tower against a dusk sky"></div>
    <a class="abs news-title" href="#">US Power Grid Costs Rise</a>
    <p class="abs news-body">Lorem ipsum dolor sit amet, consectetur adipisicing elit, sed do eiusmod tempor incididunt ut labore et dolore magna aliqua. Ut enim ad minim veniam, quis nostrud exercitation ullamco laboris nisi ut aliquip ex ea commodo consequat. Duis aute irure dolor in reprehenderit in voluptate velit esse cillum dolore eu fugiat nulla pariatur. Excepteur sint occaecat cupidatat non proident, sunt in culpa qui officia deserunt mollit anim id est laborum.</p>
    <a class="abs news-more" href="#">Learn More...</a>
  </div>
</section>

<div class="tab monitor-tab">ENERGY MONITOR</div>
<section class="panel monitor-panel">
  <div class="panel-inner">
    <svg class="chart" width="232" height="198" viewBox="0 0 232 198" font-family="Roboto, Arial, sans-serif">
      <polygon points="21,147 21,67 37,67 39,83 57,85 59,95 122,97 124,123 169,125 171,139 201,141 201,147" fill="#a6cc38"/>
      <line x1="37" y1="28" x2="37" y2="67" stroke="#a6cc38" stroke-width="1.2"/>
      <line x1="123" y1="44" x2="123" y2="97" stroke="#a6cc38" stroke-width="1.2"/>
      <line x1="202" y1="82" x2="202" y2="141" stroke="#a6cc38" stroke-width="1.2"/>
      <rect x="29" y="13" width="16" height="15" fill="#a6cc38"/><text x="37" y="24" fill="#fff" font-size="9" text-anchor="middle">49</text>
      <rect x="115" y="29" width="16" height="15" fill="#a6cc38"/><text x="123" y="40" fill="#fff" font-size="9" text-anchor="middle">27</text>
      <rect x="194" y="67" width="16" height="15" fill="#a6cc38"/><text x="202" y="78" fill="#fff" font-size="9" text-anchor="middle">6</text>
      <text x="11" y="159" fill="#a6cc38" font-size="11">2012</text>
      <text x="191" y="159" fill="#a6cc38" font-size="11">2013</text>
      <text x="116" y="186" fill="#a6cc38" font-size="10.5" text-anchor="middle">GRAPH AND CHARTS</text>
    </svg>
  </div>
</section>

<div class="tab products-tab">PRODUCTS</div>
<section class="panel products-panel">
  <div class="panel-inner">
    <div class="abs product-photo" role="img" aria-label="Photo of a black network storage unit with front drive bays"></div>
    <p class="abs product-points">Proven<br>24/7 Support System<br>Sleek Design</p>
    <a class="abs product-more" href="#">MORE...</a>
  </div>
</section>

<div class="tab portfolio-tab">PORTFOLIO</div>
<section class="panel portfolio-panel">
  <div class="panel-inner">
    <div class="abs portfolio-photo" role="img" aria-label="Photo of electrical arcs from a high-voltage coil in a dark lab"></div>
    <a class="abs portfolio-cta" href="#">VIEW<br>DETAIL</a>
  </div>
</section>

<div class="tab efficiency-tab">EFFICIENCY</div>
<section class="panel efficiency-panel">
  <div class="panel-inner">
    <svg class="chart" width="232" height="198" viewBox="0 0 232 198" font-family="Roboto, Arial, sans-serif">
      <text x="22" y="52" fill="#111" font-size="10.5">WEEK OF</text>
      <polygon points="23,140 23,118 87,64 153,113 203,80 203,140" fill="#00a9d4"/>
      <g stroke="#111" stroke-width="1.2">
        <line x1="23" y1="118" x2="23" y2="140"/><line x1="87" y1="64" x2="87" y2="140"/>
        <line x1="153" y1="113" x2="153" y2="140"/><line x1="203" y1="80" x2="203" y2="140"/>
      </g>
      <g fill="#111">
        <rect x="21" y="116" width="4" height="4"/><rect x="85" y="62" width="4" height="4"/>
        <rect x="151" y="111" width="4" height="4"/><rect x="201" y="78" width="4" height="4"/>
      </g>
      <g fill="#111" font-size="8.5" text-anchor="middle">
        <text x="23" y="150">9/1</text><text x="88" y="150">9/8</text>
        <text x="155" y="150">9/15</text><text x="205" y="150">9/30</text>
      </g>
      <text x="116" y="186" fill="#00a9d4" font-size="10.5" text-anchor="middle">GRAPH AND STATS</text>
    </svg>
  </div>
</section>

<footer>
  <div class="abs footer-links"><a href="#">Privacy Policy</a> | <a href="#">Term of Use</a> | <a href="#">FAQ</a> | <a href="#">Site Map</a></div>
  <p class="abs legal">Copyright 2013 Centro de Tecnicas Verdales. All Rights Reserved. RETC Certificate No. 58213. Centro de Tecnicas Verdales and the Green Arc design are registered trademarks or trademarks of Centro de Tecnicas Verdales Marketing Limited in the United States and/or Canada used under license, as applicable.</p>
  <p class="abs legal-note">Products and services vary depending on region or market</p>
</footer>

</body>
</html>
```